Supplment jar label design (full label)

Hydration (blue) 300g –700ml jar, label size: 10 cm x 27 cm
make label for Kora Vital supps
needs to be full blown label that fits size I noted above
with all claims in attached doc
see attached product info and claims
see QDL & Ember attached as example of similar to what I want
carbon fibre background on label
I have also attached label example this is how i expect to receive designs
where is states SKU on label needs to be in colour above
needs files to able to customise with other SKUs in future
please message me if you have questions
Hydration

```html
<!DOCTYPE html>
<html lang="en">
<head>
<meta charset="utf-8">
<title>Kora Vital Hydration – Jar Label</title>
<link href="https://fonts.googleapis.com/css2?family=Bebas+Neue&family=Montserrat:wght@400;500;600;700&display=swap" rel="stylesheet">
<style>
  :root{
    --page:#ffffff;
    --label-dark:#050505;
    --label-mid:#2a2a2a;
    --white:#ffffff;
    --sku-blue:#1b93dc;
    --muted:#b9b9b9;
    --ink:#111111;
    --badge-green:#3aa34a;
  }
  *{box-sizing:border-box;margin:0;padding:0}
  html,body{width:960px;height:1200px;overflow:hidden;background:var(--page)}
  body{font-family:"Montserrat",sans-serif;color:var(--white)}
  .label{position:absolute;left:20px;top:430px;width:920px;height:340px;overflow:hidden;background:var(--label-dark)}
  .label-texture{position:absolute;inset:0;
    background:radial-gradient(ellipse 38% 75% at 50% 48%,var(--label-mid) 0%,#151515 45%,var(--label-dark) 100%)}
  .panel{position:absolute}

  /* left info panel */
  .info{left:32px;top:46px;width:208px;font-size:8.3px;line-height:10.1px;font-weight:500}
  .info p{margin-bottom:15px}
  .info .key{color:var(--sku-blue);font-weight:700}
  .info .warning{margin-bottom:17px}
  .website{color:var(--sku-blue);font-weight:700;font-size:11px;margin:0}

  /* centre front panel */
  .front{left:359px;top:40px;width:200px;text-align:center}
  .brand{font-family:"Bebas Neue",sans-serif;font-size:71px;line-height:58px;color:var(--white);text-align:left;padding-left:16px;letter-spacing:-.5px}
  .sku{font-family:"Bebas Neue",sans-serif;font-size:52px;line-height:48px;color:var(--sku-blue);margin-top:23px;letter-spacing:-.5px}
  .tagline{font-weight:700;font-size:10.5px;margin-top:2px}
  .flavour{font-size:8.5px;color:var(--muted);margin-top:19px;letter-spacing:.3px}
  .pack{display:flex;align-items:center;justify-content:center;gap:24px;margin-top:11px}
  .servings{display:flex;align-items:center;font-size:13px;font-weight:500;letter-spacing:.5px}
  .servings .count{border:1.5px solid var(--white);font-size:19px;font-weight:700;line-height:22px;padding:0 2px;margin-right:2px}
  .weight{font-size:8px;line-height:10px;text-align:center;font-weight:500}
  .weight b{display:block;font-size:11.5px;font-weight:500;line-height:12px}

  /* right nutrition panel */
  .nutrition{left:655px;top:48px;width:226px}
  .nip{background:var(--white);color:var(--ink);border:1px solid var(--ink);font-size:7.6px;line-height:9.6px}
  .nip h2{font-size:15px;line-height:16px;font-weight:500;letter-spacing:.2px;border-bottom:1px solid var(--ink);padding:1px 2px 0}
  .nip .meta{font-size:6.4px;line-height:8px;padding:0 2px;border-bottom:1px solid var(--ink)}
  .nip table{width:100%;border-collapse:collapse}
  .nip td,.nip th{padding:0 2px;text-align:left;font-weight:500;vertical-align:top;white-space:nowrap}
  .nip th{font-size:6.4px;line-height:7.6px;padding-bottom:7px;border-left:1px solid var(--ink)}
  .nip th:first-child{border-left:none}
  .nip td{border-left:1px solid var(--ink);border-bottom:1px solid var(--ink)}
  .nip td:first-child{border-left:none;border-bottom:none;width:62px;font-weight:600}
  .nip tbody tr:first-child td{border-top:1px solid var(--ink)}
  .nip tbody tr:first-child td:first-child{border-top:none}
  .nip tbody tr:last-child td{border-bottom:none}
  .nip-note{font-size:7.6px;margin-top:4px;color:#dcdcdc}
  .claims{position:relative;font-size:7.8px;line-height:10px;margin-top:9px;font-weight:500}
  .origin-badge{position:absolute;right:0;bottom:0;width:75px;height:20px;background:var(--white);border:1px solid var(--badge-green)}
</style>
</head>
<body>
  <section class="label" aria-label="Kora Vital Hydration jar label">
    <div class="label-texture" role="img" aria-label="Dark carbon fibre texture background"></div>

    <div class="panel info">
      <p><span class="key">Ingredients:</span> Electrolyte Minerals (Sodium Chloride, Magnesium Chloride, Potassium Chloride, Calcium Citrate), Acacia Gum, Natural Flavouring, Food Acid (Citric Acid), Sweetener (Thaumatin^). ^Katemfe Fruit Extract</p>
      <p><span class="key">Directions:</span> Add 10g (approx. 2 scoops) into 500ml of chilly water depending on your liking, stir or shake to dissolve.<br>Store below 30°C in a cool, dry place.</p>
      <p><span class="key">Recommended Daily Intake:</span> 1 serving.</p>
      <p class="warning">Formulated Supplementary Sports Food.<br>This product is not a sole source of nutrition and should be consumed in conjunction with a nutritious diet and an appropriate physical training or exercise program.<br>‘Not suitable for children under 15 years of age or pregnant women: Should only be used under medical or dietetic supervision.</p>
      <p class="website">koravital.com.au</p>
    </div>

    <div class="panel front">
      <h1 class="brand">KORA<br>VITAL</h1>
      <div class="sku">HYDRATION</div>
      <div class="tagline">Optimized for Recovery</div>
      <div class="flavour">LEMON FLAVOUR</div>
      <div class="pack">
        <div class="servings"><span class="count">30</span>SERVINGS</div>
        <div class="weight">Net WT<b>300g</b></div>
      </div>
    </div>

    <div class="panel nutrition">
      <div class="nip">
        <h2>NUTRITION INFORMATION</h2>
        <div class="meta">Servings per package: 30 Serving size: 10g</div>
        <table>
          <thead>
            <tr><th></th><th>AVERAGE QUANTITY<br>PER SERVING</th><th>AVERAGE QUANTITY<br>PER 100g</th></tr>
          </thead>
          <tbody>
            <tr><td>Energy</td><td>34.6 kJ (8.3 Cal)</td><td>346 kJ (83 Cal)</td></tr>
            <tr><td>Protein</td><td>0.1 g</td><td>1.1 g</td></tr>
            <tr><td>-Gluten</td><td>Nil detected</td><td>Nil detected</td></tr>
            <tr><td>Fat, Total</td><td>0.0 g</td><td>0.0 g</td></tr>
            <tr><td>-Saturated</td><td>0.0 g</td><td>0.0 g</td></tr>
            <tr><td>Carbohydrate</td><td>0.0 g</td><td>0.0 g</td></tr>
            <tr><td>-Sugars</td><td>0.0 g</td><td>0.0 g</td></tr>
            <tr><td>Dietary Fibre</td><td>3.9 g</td><td>39.0 g</td></tr>
            <tr><td>Sodium</td><td>1,200 mg</td><td>12,000 mg</td></tr>
            <tr><td>Potassium</td><td>250 mg</td><td>2,500 mg</td></tr>
            <tr><td>Calcium</td><td>80 mg</td><td>800 mg</td></tr>
            <tr><td>Magnesium</td><td>80 mg</td><td>800 mg</td></tr>
          </tbody>
        </table>
      </div>
      <p class="nip-note">Nutrition Information relates to powder only.</p>
      <div class="claims">
        Recommended nutritional claims based on FSANZ<br>Schedule 4:<br>1. Gluten Free.<br>2. No added artificial flavour, colour &amp; sweetener.<br>3. Potassium is necessary for normal water and<br>electrolyte balance.<br>4. No Added Sugar
        <div class="origin-badge" role="img" aria-label="Country of origin badge"></div>
      </div>
    </div>
  </section>
</body>
</html>
```